ATM Website-Great Opportunity for Portability

Hey We need YOU to help us make our ATM (Automatic Teller Machine)Website!!) We are a million dollar business that will look great on your portfolio! Our Name is "CORNER CASH POINT"
Previous ATM business (now sold) was www.cashbrivo.com.au (site being pulled down so look at it fast!)
The winner will get the same package that we will giving to the winner of our other project! (worth over $9,000)
http://jobs.pixelvorn.com/job.aspx?id=4827
**we are making a series of sites/applications Winners will be solo invited to work on all upcoming projects of that catigory**
***we are also looking for Outstanding freelance guys to work with on all future projects***
Main Points!!
1: one main page (that is not a blog!)
2: Then the Theme!
3: I don't want it to look like a word-press
I.e like this guys Word press http://www.trasqueld.com/
See how he has one main page then the rest are WP Theme :)
Key points to the Home Page!
See attached pic for the menu's needed and the call now key.
Main page needs to have
1. Clean, uncluttered, and follow the feel of our LOGO (attached) Be creative but simplistic with the page. Round curves are good)
2. Large hero images of happy poeple in the community but not looking too stocky or contrived - natural smiles, natural expressions, With Image of OUR ATM on the page!
3. Easy navigation
4: (3 big buttons like on our competitors site
(http://www.brightfundpoint.com.au/) With the titles
(get an ATM (and beside it "for your business")
(Own an ATM (increase your investment Portfolio)
(Latest ATM (See an ATM in action)
For the Theme Page,
It must flow on from the main menu but have a bread crum trail on the page of all the sub links somewhere on the left of the page (or somewhere else that might look better.
Theme page should have a Call now or email now option!! If you can fit in 2 without it looking cluttered that would be good.
I will attach our brochures so you can get a feel of our product.
Also you should be able to extract images from our brochure using GLEMBRA DOC TOOL or similar PDF editor if needed!!
logo attached and also found at www.cornercashpoint.com.au
Good Fonts to use!
Helvetica Neue LT (bold thin ect)
Helvetica Neue LT Com
Target Market(s)
Business Owners and Investors
Industry/Entity Type
Investment
Requirements
Must have
- The Call now Features in the attached file, Clean layout
Should not have
- Should not look like stock photo's and a cheap website or a template...

```html
<!DOCTYPE html>
<html lang="en">
<head>
<meta charset="utf-8">
<title>Corner Cash Point</title>
<link rel="stylesheet" href="https://fonts.googleapis.com/css2?family=Inter:wght@300;400;500&display=swap">
<style>
:root{
  --green:#8dc63f;
  --green-light:#b5d98a;
  --green-dark:#3f6b3a;
  --grey:#9d9fa2;
  --grey-text:#6d6e71;
  --white:#ffffff;
  --paper:#ffffff;
}
*{box-sizing:border-box;margin:0;padding:0}
html,body{width:1200px;height:1100px;overflow:hidden;background:var(--paper);font-family:"Inter",Helvetica,Arial,sans-serif;color:var(--grey-text)}
.page{position:relative;width:1200px;height:1100px}

.brand{position:absolute;left:139px;top:60px;display:flex;align-items:center;gap:10px}
.brand-dot{width:34px;height:34px;border-radius:50%;background:var(--green)}
.brand-name{font-size:22px;font-weight:400;color:var(--grey-text);letter-spacing:.5px}

.call{position:absolute;left:431px;top:61px;display:flex;align-items:center;gap:30px}
.call-label{font-size:23px;font-weight:300;line-height:1.15;color:var(--grey)}
.call-number{font-size:29px;font-weight:300;color:var(--grey-text)}
.divider{position:absolute;left:707px;top:59px;width:2px;height:70px;background:var(--grey)}

.callback{position:absolute;left:737px;top:60px}
.callback-label{font-size:19px;font-weight:300;color:var(--grey)}
.callback-row{display:flex;gap:9px;margin-top:10px}
.field{height:33px;border:1px solid var(--grey);border-radius:8px;background:var(--white)}
.field.area{width:73px}
.field.number{width:158px}
.call-btn{width:93px;height:33px;border-radius:8px;background:var(--green);color:var(--white);font-size:17px;display:flex;align-items:center;justify-content:center;margin-left:1px}

.nav{position:absolute;left:120px;top:200px;width:961px;height:42px;display:grid;grid-template-columns:40px 82px 96px 170px 145px 122px 134px 85px 87px;border-radius:6px;overflow:hidden;background:var(--grey)}
.nav-home{background:var(--green);display:flex;align-items:center;justify-content:center}
.nav-home span{width:24px;height:24px;border-radius:50%;background:var(--white)}
.nav-item{color:var(--white);font-size:14px;display:flex;align-items:center;justify-content:center;border-left:2px solid var(--white)}

.hero{position:absolute;left:120px;top:259px;width:961px;height:337px;border-radius:7px;overflow:hidden;display:flex}
.hero-photo{width:555px;height:100%;background:linear-gradient(135deg,#e9e9e9 0%,#b9b6b1 45%,#d9a37a 75%,#8a8680 100%)}
.hero-facts{flex:1;background:var(--green);padding:38px 20px 0 19px;list-style:none}
.fact{display:flex;gap:11px;color:var(--white);font-size:16.5px;line-height:1.22;margin-bottom:18px}
.fact-num{flex:none;width:26px;height:26px;border-radius:50%;background:var(--green-dark);display:flex;align-items:center;justify-content:center;font-size:18px;margin-top:-3px}

.tiles{position:absolute;left:120px;top:625px;width:961px;height:184px}
.tile{position:absolute;top:0;width:305px;height:184px}
.tile-band{position:absolute;left:60px;right:0;top:8px;height:168px;background:var(--green);border-radius:0 8px 8px 0}
.tile-photo{position:absolute;left:0;top:0;width:184px;height:184px;border-radius:50%}
.tile-text{position:absolute;right:19px;bottom:24px;text-align:right;color:var(--white)}
.tile-title{font-size:18px;font-weight:400}
.tile-sub{font-size:13.5px;line-height:1.4}
.tile-1{left:0}.tile-2{left:329px}.tile-3{left:656px}
.tile-1 .tile-photo{background:linear-gradient(160deg,#ededed,#3f8f3a 60%,#2d6b2a)}
.tile-2 .tile-photo{background:linear-gradient(160deg,#ececec 30%,#d9b24a 60%,#6f7a80)}
.tile-3 .tile-photo{background:linear-gradient(160deg,#d8cfc1,#9da3a8 55%,#5b7a3a)}

.scene{position:absolute;left:120px;top:844px;width:961px;height:192px;background:linear-gradient(180deg,rgba(141,198,63,0) 0%,rgba(141,198,63,.25) 55%,rgba(141,198,63,.08) 100%)}
.ground{position:absolute;left:120px;top:966px;width:961px;height:3px;background:var(--green-light)}

.social{position:absolute;left:120px;top:1044px;display:flex;align-items:center}
.join{width:109px;height:33px;border-radius:4px;background:var(--green);color:var(--white);font-size:17px;font-weight:500;display:flex;align-items:center;justify-content:center;margin-right:19px}
.social-icon{width:33px;height:33px;border-radius:5px;background:var(--grey);margin-right:17px}

.legal{position:absolute;right:119px;top:1043px;text-align:right;font-size:11.5px;line-height:1.35;color:var(--grey-text)}
.legal a{color:var(--green);text-decoration:none}
</style>
</head>
<body>
<div class="page">

  <header>
    <div class="brand"><span class="brand-dot"></span><span class="brand-name">CORNER CASH POINT</span></div>

    <div class="call">
      <svg width="50" height="64" viewBox="0 0 50 64" aria-hidden="true">
        <path d="M8 4 L18 2 L24 20 L16 26 Q22 42 34 50 L42 44 L50 56 L42 62 Q12 56 4 18 Z" fill="var(--green)"/>
      </svg>
      <div>
        <div class="call-label">call us on</div>
        <div class="call-number">1300.482.716</div>
      </div>
    </div>
    <div class="divider"></div>

    <form class="callback">
      <div class="callback-label">enter your phone, we will call you</div>
      <div class="callback-row">
        <span class="field area"></span>
        <span class="field number"></span>
        <span class="call-btn">CALL ME</span>
      </div>
    </form>
  </header>

  <nav class="nav">
    <div class="nav-home"><span></span></div>
    <div class="nav-item">About</div>
    <div class="nav-item">Investor</div>
    <div class="nav-item">Products &amp; Services</div>
    <div class="nav-item">Get a Free ATM</div>
    <div class="nav-item">Giving Back</div>
    <div class="nav-item">Who Has One</div>
    <div class="nav-item">Media</div>
    <div class="nav-item">Careers</div>
  </nav>

  <section class="hero">
    <div class="hero-photo" role="img" aria-label="Close-up photo of a hand taking banknotes from an ATM cash slot"></div>
    <ol class="hero-facts">
      <li class="fact"><span class="fact-num">1</span><span>ATMs can increase foot traffic by 30%.*</span></li>
      <li class="fact"><span class="fact-num">2</span><span>70% of people that used an ATM in an outlet then purchased a product in store.*</span></li>
      <li class="fact"><span class="fact-num">3</span><span>8%-14% average increase in retail sales.**</span></li>
      <li class="fact"><span class="fact-num">4</span><span>If your competitors don’t have an ATM on site already, they soon will.</span></li>
      <li class="fact"><span class="fact-num">5</span><span>ATMs in Australia currently process over 70 million cash transactions valued in excess of $13 billion every month.</span></li>
    </ol>
  </section>

  <section class="tiles">
    <a class="tile tile-1">
      <div class="tile-band"></div>
      <div class="tile-photo" role="img" aria-label="Photo of a green free-standing ATM"></div>
      <div class="tile-text"><div class="tile-title">Get an ATM</div><div class="tile-sub">for your business</div></div>
    </a>
    <a class="tile tile-2">
      <div class="tile-band"></div>
      <div class="tile-photo" role="img" aria-label="Photo of rolled Australian banknotes"></div>
      <div class="tile-text"><div class="tile-title">Own ATM</div><div class="tile-sub">increase your<br>investment portfolio</div></div>
    </a>
    <a class="tile tile-3">
      <div class="tile-band"></div>
      <div class="tile-photo" role="img" aria-label="Photo of a shop owner standing beside a newly installed ATM"></div>
      <div class="tile-text"><div class="tile-title">Latest ATM</div><div class="tile-sub">see an ATM<br>in action</div></div>
    </a>
  </section>

  <div class="scene" role="img" aria-label="Green silhouette illustration of a house, trees, a car, birds and people walking in the community"></div>
  <div class="ground"></div>

  <footer>
    <div class="social">
      <span class="join">Join us on</span>
      <span class="social-icon"></span>
      <span class="social-icon"></span>
      <span class="social-icon"></span>
      <span class="social-icon"></span>
      <span class="social-icon"></span>
    </div>
    <div class="legal">
      Copyright (c) 2010 <a>www.cornercashpoint.com.au</a>. All rights reserved<br>
      <a>enquires@cornercashpoint.com.au</a>
    </div>
  </footer>

</div>
</body>
</html>
```